Menu Redesign - Upscale Restaurant

We are looking to have our lunch and dinner menus redesigned. We are looking to elevate the signs some, no emojis. We want a clean but elevated look, please refer to Marlowe’s Dining Collective food menu and Vento Cucina’s beverage menu. The company we’ve been using presented us with the attached menu / it’s filled with spelling and grammar errors.

Industry/Entity Type

Restaurant - Hospitality

```html
<!DOCTYPE html>
<html lang="en">
<head>
<meta charset="utf-8">
<title>Maison Odette Creole House — Menu</title>
<link href="https://fonts.googleapis.com/css2?family=Playfair+Display:wght@400;500;600&family=Poppins:wght@400;500;600&display=swap" rel="stylesheet">
<style>
:root{
  --backdrop:#a8a8a8;
  --paper:#ede8e0;
  --red:#c8202f;
  --gold:#c49a5c;
  --tan:#d9c4a3;
  --ink:#1e1e1e;
  --muted:#4a4a4a;
  --serif:'Playfair Display', Georgia, serif;
  --sans:'Poppins', Arial, sans-serif;
}
*{box-sizing:border-box;margin:0;padding:0}
html,body{width:1200px;height:2734px;overflow:hidden}
body{background:var(--backdrop);position:relative;font-family:var(--sans);color:var(--ink)}
.page{position:absolute;left:201px;width:752px;height:1064px;background:var(--paper);
  transform:scale(1.0612);transform-origin:0 0;box-shadow:0 6px 18px rgba(0,0,0,.25)}
.page-food{top:189px}
.page-drinks{top:1416px}
.abs{position:absolute}

.brand{position:absolute;left:50px;top:48px;width:240px;color:var(--red);font-family:var(--serif);font-weight:500;line-height:1}
.brand-name{font-size:38px;letter-spacing:1px;display:block}
.brand-sub{font-size:16px;letter-spacing:3px;display:block;margin-top:10px;padding-left:58px}
.header-rule{position:absolute;left:338px;top:47px;width:1px;height:93px;background:var(--red);opacity:.6}
.hours{position:absolute;left:405px;top:38px;font-family:var(--serif);line-height:1}
.hours h2{color:var(--red);font-weight:500;font-size:21px;letter-spacing:.3px}
.hours p{font-size:15px;margin-top:3px}
.hours .note{font-size:13.5px;margin-top:4px}
.hours h2.second{margin-top:9px}
.top-band{position:absolute;left:0;right:0;top:162px;height:6px;border-top:1px solid var(--red);border-bottom:1px solid var(--red);opacity:.8}

.section-title{position:absolute;font-family:var(--serif);font-weight:500;color:var(--red);font-size:23px;line-height:1;letter-spacing:.5px}
.flourish{position:absolute;height:8px;background:linear-gradient(90deg,rgba(196,154,92,.15),rgba(196,154,92,.55),rgba(196,154,92,.15));border-radius:4px}

.item{position:absolute}
.item-row{display:flex;align-items:baseline;font-size:10.5px;font-weight:500;text-transform:uppercase;letter-spacing:.1px;white-space:nowrap}
.leader{flex:1;min-width:6px;border-bottom:.7px solid #555;margin:0 3px;transform:translateY(-3px)}
.item-price{font-weight:500}
.item-price sup{font-size:6px;vertical-align:5px}
.item-desc{font-size:5.6px;line-height:1.35;color:var(--muted);margin-top:2px}
.row-tight{font-size:8.6px;letter-spacing:-.2px}

.frame{position:absolute;overflow:visible}
.frame path{fill:none;stroke:var(--gold);stroke-width:2}

.centered{text-align:center}
.small-caps-note{position:absolute;font-size:8px;letter-spacing:.3px;color:var(--muted);text-transform:uppercase}

.protein-box{position:absolute;left:259px;top:786px;width:192px;height:44px;background:var(--tan);border-radius:6px;padding:8px 10px;font-size:8.5px}
.protein-box strong{font-weight:500;font-size:9px;display:block}
.protein-box span{font-size:6.2px;line-height:1.35;color:#333}
.dressing{position:absolute;left:259px;top:849px;width:210px;font-size:6.8px;line-height:1.3}
.dressing b{font-weight:600}
.notice{position:absolute;left:502px;top:831px;width:193px;height:30px;background:var(--tan);border-radius:7px;font-size:5.6px;line-height:1.3;text-align:center;padding:5px 8px}

.sides-title{position:absolute;left:334px;top:885px;width:80px;background:var(--paper);text-align:center}
.side-col{position:absolute;top:911px;font-size:10px;font-weight:600;line-height:15.3px}
.side-col sup{font-size:6px;vertical-align:4px;color:var(--red)}
.side-col .price{color:var(--red)}
.side-rule{position:absolute;top:912px;width:1px;height:70px;background:var(--gold);opacity:.7}
.disclaimer{position:absolute;left:0;width:752px;text-align:center;font-size:7.8px;color:#333}

.sub-list{position:absolute;font-size:5.6px;line-height:1.9;color:var(--muted)}
.wine-head{display:flex;align-items:baseline;font-size:10.5px;font-weight:500;width:104px}
.by-glass{position:absolute;left:504px;width:204px;text-align:center;font-size:9px;top:498px}
.ornament{position:absolute;border-radius:40px;background:radial-gradient(ellipse at center,rgba(196,154,92,.75),rgba(196,154,92,.25))}
</style>
</head>
<body>

<section class="page page-food">
  <div class="brand"><span class="brand-name">MAISON ODETTE</span><span class="brand-sub">CREOLE HOUSE</span></div>
  <div class="header-rule"></div>
  <div class="hours">
    <h2>HAPPY HOUR FOOD &amp; DRINKS</h2>
    <p>MONDAY TO FRIDAY 3:00PM-6:00PM</p>
    <p class="note">Bar seats and high top tables by bar ONLY</p>
    <h2 class="second">BRUNCH</h2>
    <p>SATURDAY &amp; SUNDAY 11:00AM-3:30PM</p>
  </div>
  <div class="top-band"></div>

  <h3 class="section-title" style="left:41px;top:186px">SMALL PLATES</h3>
  <div class="flourish" role="img" aria-label="Decorative gold scroll flourish" style="left:41px;top:213px;width:177px"></div>

  <div class="item" style="left:41px;top:236px;width:172px"><div class="item-row"><span>Creole Wings</span><span class="leader"></span><span class="item-price"><sup>$</sup>16</span></div><p class="item-desc">Fried crispy bone-in traditional wings tossed in your choice of our signature sauces: Plain, Mambo, Voodoo, Hot honey lemon pepper.</p></div>
  <div class="item" style="left:41px;top:281px;width:172px"><div class="item-row"><span>Spinach Dip</span><span class="leader"></span><span class="item-price"><sup>$</sup>13</span></div><p class="item-desc">Fresh chopped spinach cooked in a four cheese blend served with fresh tortilla chips. Add Jumbo Lump Crab +$8.</p></div>
  <div class="item" style="left:41px;top:318px;width:172px"><div class="item-row"><span>Fried Green Tomatoes</span><span class="leader"></span><span class="item-price"><sup>$</sup>13</span></div><p class="item-desc">Sliced green tomatoes seasoned in house blend battered in panko bread crumb. Add Jumbo Lump Crab +$5.</p></div>
  <div class="item" style="left:41px;top:355px;width:172px"><div class="item-row"><span>Seafood Rolls</span><span class="leader"></span><span class="item-price"><sup>$</sup>16</span></div><p class="item-desc">Chopped shrimp, crab meat and cheese in a egg roll served with remoulade dipping.</p></div>
  <div class="item" style="left:41px;top:392px;width:172px"><div class="item-row"><span>Bayou Rolls</span><span class="leader"></span><span class="item-price"><sup>$</sup>15</span></div><p class="item-desc">Diced chicken, peppers and cheese stuffed in a egg roll served with remoulade dipping.</p></div>
  <div class="item" style="left:41px;top:429px;width:172px"><div class="item-row"><span>Fried Devil Eggs</span><span class="leader"></span><span class="item-price"><sup>$</sup>13</span></div><p class="item-desc">Sweet relish, spiced whipped eggs with a choice of being topped with fresh Jumbo Lump Crab Meat or Shrimp for a upcharge.</p></div>
  <div class="item" style="left:41px;top:474px;width:172px"><div class="item-row"><span>Hot Honey Salmon Bites</span><span class="leader"></span><span class="item-price"><sup>$</sup>15</span></div><p class="item-desc">Sweet relish, spiced whipped eggs with a choice of being topped with fresh Jumbo Lump Crab Meat or Shrimp for a upcharge.</p></div>
  <div class="item" style="left:41px;top:518px;width:172px"><div class="item-row"><span>Stuffed Shrimp</span><span class="leader"></span><span class="item-price"><sup>$</sup>18</span></div><p class="item-desc">Shrimp stuffed with jumbo lump crab meat coated in house batter, fried golden brown, over a bed jalapeño corn succotash.</p></div>
  <div class="item" style="left:41px;top:557px;width:172px"><div class="item-row"><span>Seafood Basket</span><span class="leader"></span><span class="item-price"><sup>$</sup>18</span></div><p class="item-desc">Choice of fresh battered catfish or fried golden shrimp with season fries.</p></div>
  <div class="item" style="left:41px;top:592px;width:172px"><div class="item-row"><span>New Orleans Shrimp</span><span class="leader"></span><span class="item-price"><sup>$</sup>16</span></div><p class="item-desc">Creamy garlic cajun sauteed shrimp served with toasted bread.</p></div>
  <div class="item" style="left:41px;top:623px;width:172px"><div class="item-row"><span>Voodoo Shrimp</span><span class="leader"></span><span class="item-price"><sup>$</sup>16</span></div><p class="item-desc">Fried shrimp tossed in voodoo sauce topped with fresh jalapenos and blue cheese crumble.</p></div>
  <div class="item" style="left:41px;top:659px;width:172px"><div class="item-row"><span>Cup of Gumbo</span><span class="leader"></span><span class="item-price"><sup>$</sup>15</span></div><p class="item-desc">Andouille sausage, shrimp, chicken slow cooked in a cajun broth topped with rice.</p></div>
  <div class="item" style="left:41px;top:695px;width:172px"><div class="item-row"><span>Raw Oyster</span><span class="leader"></span><span class="item-price"><sup>$</sup>16</span></div><p class="item-desc">Fresh shucked blue point oysters served over ice with fresh lemons, horseradish, hot sauce, and mignonette.</p></div>
  <div class="item" style="left:41px;top:731px;width:172px"><div class="item-row"><span>Chargrilled Oysters</span><span class="leader"></span><span class="item-price"><sup>$</sup>17</span></div><p class="item-desc">Fresh shucked blue point oysters grilled with Cajun garlic butter and four cheese blend.</p></div>
  <div class="item" style="left:41px;top:767px;width:172px"><div class="item-row"><span>Rockefeller Oysters</span><span class="leader"></span><span class="item-price"><sup>$</sup>18</span></div><p class="item-desc">Fresh shucked blue point oysters stuffed with creamy spinach and cheese.</p></div>
  <div class="item" style="left:41px;top:802px;width:172px"><div class="item-row"><span>Jambalaya Oysters</span><span class="leader"></span><span class="item-price"><sup>$</sup>22</span></div><p class="item-desc">Fresh shucked blue point oysters stuffed with creamy cajun shrimp and crab.</p></div>
  <div class="item" style="left:41px;top:838px;width:172px"><div class="item-row"><span>Make it a Platter</span><span class="leader"></span><span class="item-price"><sup>$</sup>22</span></div><p class="item-desc">(Serves 3)<br>Mix 3 of your favorite starters.<br>(Each Seafood starter added to platter are upcharged)</p></div>

  <svg class="frame" style="left:261px;top:188px" width="200" height="260" viewBox="0 0 200 260"><path d="M14 1H186A13 13 0 0 0 199 14V246A13 13 0 0 0 186 259H14A13 13 0 0 0 1 246V14A13 13 0 0 0 14 1Z"/></svg>
  <h3 class="section-title centered" style="left:261px;top:210px;width:200px">SANDWICHES</h3>
  <p class="small-caps-note centered" style="left:261px;top:251px;width:200px">All served with cajun fries</p>
  <div class="item" style="left:274px;top:281px;width:172px"><div class="item-row"><span>Loaded Burger</span><span class="leader"></span><span class="item-price"><sup>$</sup>18</span></div><p class="item-desc">Beef patty topped with white cheddar cheese, lettuce, tomato, fried egg, and mambo sauce. Served with fries.</p></div>
  <div class="item" style="left:274px;top:327px;width:172px"><div class="item-row row-tight"><span>Maison Odette Chicken Sandwich</span><span class="leader"></span><span class="item-price"><sup>$</sup>18</span></div><p class="item-desc">Fresh chopped spinach cooked in a four cheese blend served with fresh tortilla chips. Add Jumbo Lump Crab +$8.</p></div>
  <div class="item" style="left:274px;top:376px;width:172px"><div class="item-row"><span>Crabcake Sandwich</span><span class="leader"></span><span class="item-price"><sup>$</sup>25</span></div><p class="item-desc">Fresh jumbo lump crab cake, deep-fried or pan-seared. Topped with lettuce, tomato, crispy bacon, and remoulade sauce served with fries.</p></div>

  <svg class="frame" style="left:259px;top:486px" width="200" height="264" viewBox="0 0 200 264"><path d="M14 1H186A13 13 0 0 0 199 14V250A13 13 0 0 0 186 263H14A13 13 0 0 0 1 250V14A13 13 0 0 0 14 1Z"/></svg>
  <h3 class="section-title centered" style="left:259px;top:505px;width:200px">SALADS</h3>
  <div class="flourish" role="img" aria-label="Decorative gold scroll flourish" style="left:312px;top:530px;width:95px"></div>
  <div class="item" style="left:272px;top:552px;width:172px"><div class="item-row"><span>Ceasar</span><span class="leader"></span><span class="item-price"><sup>$</sup>12</span></div><p class="item-desc">Romaine, Parmesan-romano, croutons, housemade Ceasar dressing.</p></div>
  <div class="item" style="left:272px;top:593px;width:172px"><div class="item-row"><span>Crispy Chicken House</span><span class="leader"></span><span class="item-price"><sup>$</sup>17</span></div><p class="item-desc">Field greens, dried cranberries, cherry tomatoes, cucumbers, boiled egg, cheddar cheese, croutons, fried crispy chicken breast, and Housemade Champagne</p></div>
  <div class="item" style="left:272px;top:642px;width:172px"><div class="item-row" style="font-size:10px;letter-spacing:-.1px"><span>Honey Caribbean Salmon</span><span class="leader"></span><span class="item-price"><sup>$</sup>22</span></div><p class="item-desc">Field greens, corn off the cob, tomatoes, cucumbers, red onions, and buttermilk herb dressing</p></div>
  <div class="item" style="left:272px;top:682px;width:172px"><div class="item-row"><span>Grilled Pear &amp; Walnut</span><span class="leader"></span><span class="item-price"><sup>$</sup>19</span></div><p class="item-desc">A vibrant salad of fresh greens, charred pear slices, cucumbers, red onions, cherry tomatoes, dried cranberries, walnuts, and blackened chicken.</p></div>

  <div class="protein-box"><strong>Add Protein:</strong><span>Shrimp +7, Salmon +12, Blackened Chicken+10, Steak +16</span></div>
  <p class="dressing"><b>Dressing Options:</b> Honey Mustard, Balsamic Vinaigrette, Ranch, Caesar, Blue Cheese</p>

  <h3 class="section-title" style="left:502px;top:186px">ENTREES</h3>
  <div class="flourish" role="img" aria-label="Decorative gold scroll flourish" style="left:502px;top:210px;width:112px"></div>

  <div class="item" style="left:502px;top:235px;width:174px"><div class="item-row"><span>Creole Herb Chicken</span><span class="leader"></span><span class="item-price"><sup>$</sup>28</span></div><p class="item-desc">Creole and herb seasoned 1/2 chicken roasted tender and topped with creamy creole sauce and served with 2 sides of your choice.</p></div>
  <div class="item" style="left:502px;top:279px;width:174px"><div class="item-row"><span>Creole Salmon</span><span class="leader"></span><span class="item-price"><sup>$</sup>13</span></div><p class="item-desc">Perfectly seasoned pan-seared salmon topped with creamy creole sauce served with 2 side</p></div>
  <div class="item" style="left:502px;top:317px;width:174px"><div class="item-row"><span>Bayou Pasta</span><span class="leader"></span><span class="item-price"><sup>$</sup>26</span></div><p class="item-desc">House-made cream sauce, bell peppers, tomatoes, and onions over a bed of linguine pasta topped with blackened chicken breast.</p></div>
  <div class="item" style="left:502px;top:361px;width:174px"><div class="item-row"><span>Pork Chops</span><span class="leader"></span><span class="item-price"><sup>$</sup>25</span></div><p class="item-desc">Fried or grilled pork chops smothered in southern gravy served with two sides of your choice</p></div>
  <div class="item" style="left:502px;top:399px;width:174px"><div class="item-row"><span>Crab Cakes</span><span class="leader"></span><span class="item-price"><sup>$</sup>MKT</span></div><p class="item-desc">2 Broiled crab cake, fresh jumbo lump crab meat, served with two sides.</p></div>
  <div class="item" style="left:502px;top:437px;width:174px"><div class="item-row row-tight" style="font-size:9.4px"><span>Maison Odette Fried Chicken</span><span class="leader"></span><span class="item-price"><sup>$</sup>23</span></div><p class="item-desc">1/2 chicken marinated in southern seasonings, fried golden served with two sides of your choice.</p></div>
  <div class="item" style="left:502px;top:475px;width:174px"><div class="item-row"><span>Fried Catfish</span><span class="leader"></span><span class="item-price"><sup>$</sup>25</span></div><p class="item-desc">Catfish fried golden or blackened served with two sides of your choice.</p></div>
  <div class="item" style="left:502px;top:513px;width:174px"><div class="item-row"><span>Loaded Creole Pasta</span><span class="leader"></span><span class="item-price"><sup>$</sup>50</span></div><p class="item-desc">Sautéed shrimp, jumbo lump crab meat, and crab leg over creamy cajun linguine.</p></div>
  <div class="item" style="left:502px;top:552px;width:174px"><div class="item-row"><span>Jambalaya Pasta</span><span class="leader"></span><span class="item-price"><sup>$</sup>27</span></div><p class="item-desc">Shrimp, chicken, andouille sausage, veggies, in a Cajun cream sauce. Rice option available.</p></div>
  <div class="item" style="left:502px;top:590px;width:174px"><div class="item-row"><span>Gumbo w/ Cornbread</span><span class="leader"></span><span class="item-price"><sup>$</sup>25</span></div><p class="item-desc">Rich Roux with chicken and veggies and seafood broth with andouille sausage, fresh shrimp, and scallion rice. Add Crab Leg +$10</p></div>
  <div class="item" style="left:502px;top:634px;width:174px"><div class="item-row"><span>Shrimp &amp; Grits</span><span class="leader"></span><span class="item-price"><sup>$</sup>28</span></div><p class="item-desc">Sautéed shrimp, onions, peppers, and tomatoes in creamy cajun sauce. over cheesy grits. Add Crab Meat +$10</p></div>
  <div class="item" style="left:502px;top:673px;width:174px"><div class="item-row"><span>Red Snapper</span><span class="leader"></span><span class="item-price"><sup>$</sup>MKT</span></div><p class="item-desc">Choice of deep fried or roasted red snapper served with jambalaya stew sauce and two sides of your choice.</p></div>
  <div class="item" style="left:502px;top:711px;width:174px"><div class="item-row"><span>Oxtails</span><span class="leader"></span><span class="item-price"><sup>$</sup>40</span></div><p class="item-desc">Braised oxtails with butter beans Southern-style served with your choice of two sides.</p></div>
  <div class="item" style="left:502px;top:747px;width:174px"><div class="item-row"><span>Catfish &amp; Grits</span><span class="leader"></span><span class="item-price"><sup>$</sup>28</span></div><p class="item-desc">Fresh wild caught blackened or fried, served over a bed of white cheddar grits topped with cajun cream sauce. Add Crab Meat +$10</p></div>
  <div class="item" style="left:502px;top:791px;width:174px"><div class="item-row"><span>Caribbean Lamb Chops</span><span class="leader"></span><span class="item-price"><sup>$</sup>45</span></div><p class="item-desc">Lamb chops seasoned to perfection, topped with sweet caribbean glaze. Served with two sides of your choice.</p></div>
  <p class="notice">Please read menu descriptions carefully and be sure about what you are ordering. All checks will have 20% gratuity added. All parties 4+ will be on one check.</p>

  <svg class="frame" style="left:41px;top:894px" width="670" height="106" viewBox="0 0 670 106"><path d="M14 1H656A13 13 0 0 0 669 14V92A13 13 0 0 0 656 105H14A13 13 0 0 0 1 92V14A13 13 0 0 0 14 1Z"/></svg>
  <h3 class="section-title sides-title">SIDES</h3>
  <div class="side-col" style="left:78px">Cajun crab fries <sup>$</sup><span class="price">18</span><br>Spinach <sup>$</sup><span class="price">7</span><br>Lemon herb broccolini <sup>$</sup><span class="price">9</span><br>Asparagus <sup>$</sup><span class="price">9</span><br>Five cheese mac <sup>$</sup><span class="price">9</span></div>
  <div class="side-rule" style="left:241px"></div>
  <div class="side-col" style="left:276px">fried rice <sup>$</sup><span class="price">8</span><br>seafood fried rice <sup>$</sup><span class="price">15</span><br>mashed potatoes <sup>$</sup><span class="price">8</span><br>seafood mac n cheese <sup>$</sup><span class="price">15</span><br>red beans and rice <sup>$</sup><span class="price">9</span></div>
  <div class="side-rule" style="left:443px"></div>
  <div class="side-col" style="left:478px">cheesy grits <sup>$</sup><span class="price">4</span><br>honey cornbread <sup>$</sup><span class="price">6</span><br>cajun fries <sup>$</sup><span class="price">4</span><br>sweet potato casserole <sup>$</sup><span class="price">7</span><br>collard greens with smoked turkey <sup>$</sup><span class="price">8</span></div>

  <p class="disclaimer" style="top:1010px">Please alert your server if you have any food allergies. Consuming raw or undercooked meats, poultry, seafood, shellfish or eggs may increase your risk of foodborne illness.</p>
</section>

<section class="page page-drinks">
  <div class="brand"><span class="brand-name">MAISON ODETTE</span><span class="brand-sub">CREOLE HOUSE</span></div>
  <div class="header-rule"></div>
  <div class="hours">
    <h2>HAPPY HOUR FOOD &amp; DRINKS</h2>
    <p>MONDAY TO FRIDAY 3:00PM-6:00PM</p>
    <p class="note">Bar seats and high top tables by bar ONLY</p>
    <h2 class="second">BRUNCH</h2>
    <p>SATURDAY &amp; SUNDAY 11:00AM-3:30PM</p>
  </div>
  <div class="top-band"></div>

  <h3 class="section-title" style="left:41px;top:204px">BEVERAGES</h3>
  <div class="flourish" role="img" aria-label="Decorative gold scroll flourish" style="left:41px;top:232px;width:140px"></div>
  <div class="item" style="left:41px;top:270px;width:170px"><div class="item-row"><span>Soft Drinks</span><span class="leader"></span><span class="item-price" style="text-transform:none">4 (free refills)</span></div><p class="item-desc">Cola| Diet Cola| Lemon-Lime| Orange Juice| Ginger Ale| Pineapple Juice| Cranberry | Juice</p></div>
  <div class="item" style="left:41px;top:324px;width:170px"><div class="item-row" style="font-size:9.3px;letter-spacing:-.1px"><span>Creole Lemonade &amp; Sweet Tea</span><span class="leader"></span><span class="item-price">5</span></div><p class="item-desc">Strawberry | Peach | Mango | Watermelon | Kiwi | Blueberry</p></div>
  <div class="item" style="left:41px;top:373px;width:170px"><div class="item-row"><span>Ginger Beer</span><span class="leader"></span><span class="item-price">4</span></div></div>
  <div class="item" style="left:41px;top:410px;width:170px"><div class="item-row"><span>Blueberry Fizz</span><span class="leader"></span><span class="item-price">12</span></div><p class="item-desc">Blueberry, lime, ginger beer</p></div>
  <div class="item" style="left:41px;top:459px;width:170px"><div class="item-row"><span>Pineapple Punch</span><span class="leader"></span><span class="item-price">12</span></div><p class="item-desc">Orange &amp; pineapple juice,mai tai, peach, fresh lime.</p></div>
  <div class="item" style="left:41px;top:509px;width:170px"><div class="item-row"><span>Aqua Fonte</span><span class="leader"></span><span class="item-price">5</span></div></div>
  <div class="item" style="left:41px;top:547px;width:170px"><div class="item-row"><span>S. Valverde</span><span class="leader"></span><span class="item-price">5</span></div></div>

  <h3 class="section-title" style="left:41px;top:604px">SPIRITS</h3>
  <div class="flourish" role="img" aria-label="Decorative gold scroll flourish" style="left:41px;top:632px;width:140px"></div>
  <div class="item" style="left:41px;top:664px;width:170px"><div class="item-row"><span>Bourbon &amp; Whiskey</span></div><p class="item-desc">Oakmere Reserve Hollis Hayes Ballard Ballard Rye Uncle Ezra Regal Maple Fenwick Irish Regal Apple Jessup Black Harlan Creek</p></div>
  <div class="item" style="left:41px;top:711px;width:170px"><div class="item-row"><span>Scotch</span></div><p class="item-desc">Hollins Black<br>Glenmora Craigdarroch 12</p></div>
  <div class="item" style="left:41px;top:751px;width:170px"><div class="item-row"><span>Vodka</span></div><p class="item-desc">Belmonte Kettering One Tilden's Silver Heron Verlaine Double Espresso</p></div>
  <div class="item" style="left:41px;top:794px;width:170px"><div class="item-row"><span>Gin</span></div><p class="item-desc">Bayside Sapphire Hollister Tamsin Regent</p></div>
  <div class="item" style="left:41px;top:828px;width:170px"><div class="item-row"><span>Tequila</span></div><p class="item-desc">Casa Amiga Don Rafael Milagrosa Patrona Espuela Don Rafael 1942 Cielo Azul</p></div>
  <div class="item" style="left:41px;top:868px;width:170px"><div class="item-row"><span>Rum</span></div><p class="item-desc">Bayamo<br>Captain Marlow Spiced Mayfair Dark</p></div>

  <h3 class="section-title" style="left:269px;top:204px;line-height:1.15">SPECIALTY<br>COCKTAILS</h3>
  <div class="flourish" role="img" aria-label="Decorative gold scroll flourish" style="left:269px;top:261px;width:148px"></div>
  <div class="item" style="left:269px;top:296px;width:172px"><div class="item-row" style="font-size:10px"><span>Odette's Hurricane</span><span class="leader"></span><span class="item-price"><sup>$</sup>16</span></div><p class="item-desc">Dark rum light rum, passion, fruit punch lime juice, orange juice, grenadine.</p></div>
  <div class="item" style="left:269px;top:338px;width:172px"><div class="item-row"><span>Tsunami</span><span class="leader"></span><span class="item-price"><sup>$</sup>16</span></div><p class="item-desc">Blanco tequila, pineapple, orange, passionfruit, blue curacao topped with dark tequila.</p></div>
  <div class="item" style="left:269px;top:379px;width:172px"><div class="item-row"><span>Secrets</span><span class="leader"></span><span class="item-price"><sup>$</sup>15</span></div><p class="item-desc">Secret blend of 3 rums, tropical punch, and fresh lime.</p></div>
  <div class="item" style="left:269px;top:414px;width:172px"><div class="item-row"><span>Smoked in Fashion</span><span class="leader"></span><span class="item-price"><sup>$</sup>18</span></div><p class="item-desc">Bourbon, cubed sugar, black cherry, orange and cherry bitters.</p></div>
  <div class="item" style="left:269px;top:448px;width:172px"><div class="item-row row-tight" style="font-size:9.2px"><span>Smoked Tequila Old Fashion</span><span class="leader"></span><span class="item-price"><sup>$</sup>18</span></div><p class="item-desc">Aged tequila, orange liqueur, agave nectar, peach bitters, fresh orange peel.</p></div>
  <div class="item" style="left:269px;top:488px;width:172px"><div class="item-row"><span>Miskiri</span><span class="leader"></span><span class="item-price"><sup>$</sup>17</span></div><p class="item-desc">Tequila, Grand Soleil, blackberry, pineapple, cranberry, lemon juice.</p></div>
  <div class="item" style="left:269px;top:524px;width:172px"><div class="item-row"><span>Blackberry French</span><span class="leader"></span><span class="item-price"><sup>$</sup>15</span></div><p class="item-desc">Regent 1908 Gin, lemonade champagne, blackberries, white flower.</p></div>
  <div class="item" style="left:269px;top:566px;width:172px"><div class="item-row row-tight"><span>Margarita or Lemon Drop Flight</span><span class="leader"></span><span class="item-price"><sup>$</sup>20</span></div><p class="item-desc">Sautéed shrimp, jumbo lump crab meat, and crab leg over creamy cajun linguine.</p></div>
  <div class="item" style="left:269px;top:608px;width:172px"><div class="item-row"><span>Lousiana Tea</span><span class="leader"></span><span class="item-price"><sup>$</sup>17</span></div><p class="item-desc">Uncle Ezra, honey mint syrup, fresh lemonade.</p></div>
  <div class="item" style="left:269px;top:643px;width:172px"><div class="item-row"><span>Pink Lady</span><span class="leader"></span><span class="item-price"><sup>$</sup>15</span></div><p class="item-desc">Tequila, orange liqueur, lime, stawberry-kiwi, agave.</p></div>
  <div class="item" style="left:269px;top:678px;width:172px"><div class="item-row"><span>Creole Island</span><span class="leader"></span><span class="item-price"><sup>$</sup>19</span></div><p class="item-desc">Grand Soleil, Hollande VS, tropical punch.</p></div>
  <div class="item" style="left:269px;top:712px;width:172px"><div class="item-row"><span>Becky Sangria</span><span class="leader"></span><span class="item-price"><sup>$</sup>18</span></div><p class="item-desc">Red wine blend, Hollande VS, tropical fruit punch, and frozen popsicle.</p></div>
  <div class="item" style="left:269px;top:753px;width:172px"><div class="item-row"><span>Pineapple-Gria</span><span class="leader"></span><span class="item-price"><sup>$</sup>18</span></div><p class="item-desc">White sparkling wine, rum, pineapple punch.</p></div>
  <div class="item" style="left:269px;top:787px;width:172px"><div class="item-row"><span>Peach Please</span><span class="leader"></span><span class="item-price"><sup>$</sup>16</span></div><p class="item-desc">Grand Soleil, Hollande VS, tropical punch.</p></div>
  <div class="item" style="left:269px;top:819px;width:172px"><div class="item-row"><span>Toasted Marshmallow</span></div><div class="item-row"><span>Espresso Martini</span><span class="leader"></span><span class="item-price"><sup>$</sup>16</span></div><p class="item-desc">Toasted marshmallow, espresso, vodka, cream, white chocolate liqueur.</p></div>
  <div class="item" style="left:269px;top:875px;width:172px"><div class="item-row"><span>Odette's Passion</span><span class="leader"></span><span class="item-price"><sup>$</sup>18</span></div><p class="item-desc">Duvall VSOP, orange liqueur, lemon juice, passionfruit.</p></div>

  <svg class="frame" style="left:504px;top:208px" width="202" height="144" viewBox="0 0 202 144"><path d="M14 1H188A13 13 0 0 0 201 14V130A13 13 0 0 0 188 143H14A13 13 0 0 0 1 130V14A13 13 0 0 0 14 1Z"/></svg>
  <h3 class="section-title centered" style="left:504px;top:224px;width:202px">BEERS</h3>
  <div class="flourish" role="img" aria-label="Decorative gold scroll flourish" style="left:529px;top:248px;width:152px"></div>
  <p class="small-caps-note centered" style="left:504px;top:265px;width:202px">All served with cajun fries</p>
  <div class="abs wine-head" style="left:533px;top:286px"><span>BOTTLE</span><span class="leader"></span><span>7</span></div>
  <div class="sub-list" style="left:533px;top:302px">Bayou Light<br>Red Tide<br>Seasonal IPA</div>
  <div class="sub-list" style="left:584px;top:302px">Blue Harbor<br>Costa Clara</div>
  <div class="sub-list" style="left:630px;top:302px">Cross Orchard<br>Helmsen</div>

  <svg class="frame" style="left:504px;top:420px" width="204" height="284" viewBox="0 0 204 284"><path d="M14 1H190A13 13 0 0 0 203 14V270A13 13 0 0 0 190 283H14A13 13 0 0 0 1 270V14A13 13 0 0 0 14 1Z"/></svg>
  <h3 class="section-title centered" style="left:504px;top:457px;width:204px">WINE &amp; BUBBLY</h3>
  <div class="flourish" role="img" aria-label="Decorative gold scroll flourish" style="left:529px;top:482px;width:154px"></div>
  <p class="by-glass">By the glass 10</p>
  <div class="abs wine-head" style="left:527px;top:519px"><span>REDS</span><span class="leader"></span><span>10</span></div>
  <div class="sub-list" style="left:527px;top:535px">Cabernet<br>Merlot</div>
  <div class="sub-list" style="left:569px;top:535px">Pinot Noir<br>Sweet Red Blend</div>
  <div class="abs wine-head" style="left:527px;top:565px"><span>WHITE</span><span class="leader"></span><span>10</span></div>
  <div class="sub-list" style="left:527px;top:580px">Moscato Pinot Grigio<br>Sauvignon Blanc<br>Chardonnay</div>
  <div class="abs wine-head" style="left:527px;top:622px"><span>BUBBLY</span><span class="leader"></span><span>10</span></div>
  <div class="sub-list" style="left:527px;top:638px">(by the glass)<br>Prosecco 13<br>Brut 5</div>

  <div class="ornament" role="img" aria-label="Large gold scroll ornament with a flame-shaped drop" style="left:556px;top:727px;width:100px;height:170px"></div>
  <div class="flourish" role="img" aria-label="Gold scrollwork divider" style="left:161px;top:945px;width:430px"></div>

  <p class="disclaimer" style="top:988px;line-height:1.45">Please alert your server if you have any food allergies.<br>Consuming raw or undercooked meats, poultry, seafood, shellfish or eggs may increase your risk of foodborne illness</p>
</section>

</body>
</html>
```